Lantern Hill Publicity is a new boutique Press Office with a small roster of well-chosen clients across an array of disciplines; from Art and Technology to Restaurants and Fashion. Based in Greenpoint Brooklyn, Lantern Hill Publicity achieves outstanding results through hard work, tenacity, efficiency and a sense of humor. We need a simple, versatile and classic design. We would like each side of the card to be white text on a black background.

Boutique

```html
<!DOCTYPE html>
<html lang="en">
<head>
<meta charset="utf-8">
<title>Lantern Hill Publicity – Business Card</title>
<link href="https://fonts.googleapis.com/css2?family=Cinzel:wght@400&family=Open+Sans:wght@400;600&display=swap" rel="stylesheet">
<style>
  :root {
    --bg: #e9e7e4;
    --ink: #000000;
    --band: #1b1b1b;
    --paper: #ffffff;
  }
  html, body {
    margin: 0;
    width: 1200px;
    height: 900px;
    overflow: hidden;
    background: var(--bg);
  }
  .canvas { position: relative; width: 1200px; height: 900px; }
  .card {
    position: absolute;
    overflow: hidden;
    background: var(--ink);
    box-shadow: 0 6px 18px rgba(0,0,0,0.18);
  }
  .card--front { left: 77px; top: 33px; width: 589px; height: 364px; }
  .card--back { left: 388px; top: 505px; width: 567px; height: 352px; }

  .wordmark {
    position: absolute; left: 0; right: 0;
    margin: 0;
    text-align: center;
    font-family: 'Cinzel', serif;
    font-weight: 400;
    line-height: 1;
    color: var(--paper);
  }
  .wordmark__main, .wordmark__sub { display: block; white-space: nowrap; }
  .card--front .wordmark { top: 152px; }
  .card--front .wordmark__main { font-size: 33px; letter-spacing: 5px; }
  .card--front .wordmark__sub { font-size: 16px; letter-spacing: 11px; margin-top: 1px; }
  .card--back .wordmark { top: 192px; }
  .card--back .wordmark__main { font-size: 42px; letter-spacing: 7px; }
  .card--back .wordmark__sub { font-size: 19px; letter-spacing: 14px; margin-top: 0; }

  .front-base { position: absolute; left: 0; top: 0; }
  .person {
    position: absolute; right: 316px; top: 262px;
    text-align: right; color: var(--paper);
    font-family: 'Open Sans', sans-serif;
  }
  .person__name { font-size: 19px; font-weight: 600; line-height: 26px; }
  .person__title { font-size: 15px; line-height: 20px; }
  .contacts {
    position: absolute; left: 293px; top: 250px;
    list-style: none; margin: 0; padding: 0;
    font-family: 'Open Sans', sans-serif;
    font-size: 15px; color: var(--paper);
  }
  .contacts li { display: flex; align-items: center; height: 21px; white-space: nowrap; }
  .contacts svg { width: 12px; height: 12px; margin-right: 14px; fill: var(--paper); }
  .address {
    position: absolute; left: 0; right: 12px; top: 327px;
    margin: 0;
    text-align: center;
    font-family: 'Open Sans', sans-serif;
    font-size: 15px; color: var(--paper);
  }
</style>
</head>
<body>
<main class="canvas">
  <section class="card card--front">
    <svg class="front-base" width="589" height="364" viewBox="0 0 589 364" aria-hidden="true">
      <polygon points="0,200 389,200 365,225 0,225" fill="var(--band)"/>
      <polygon points="0,225 365,225 389,200 413,192 384,229 0,229" fill="var(--paper)"/>
    </svg>
    <h1 class="wordmark">
      <span class="wordmark__main">Lantern Hill</span>
      <span class="wordmark__sub">Publicity</span>
    </h1>
    <div class="person">
      <div class="person__name">Daniel Carter</div>
      <div class="person__title">Managing Director</div>
    </div>
    <ul class="contacts">
      <li><svg viewBox="0 0 24 24"><path d="M6.6 10.8a15 15 0 0 0 6.6 6.6l2.2-2.2c.3-.3.7-.4 1-.2 1.1.4 2.3.6 3.6.6.6 0 1 .4 1 1V20c0 .6-.4 1-1 1C10.6 21 3 13.4 3 4c0-.6.4-1 1-1h3.5c.6 0 1 .4 1 1 0 1.3.2 2.5.6 3.6.1.3 0 .7-.2 1z"/></svg>044-555 019 284</li>
      <li><svg viewBox="0 0 24 24"><path d="M2 5h20v14H2z M4 7v1l8 5 8-5V7l-8 5z" fill-rule="evenodd"/></svg>info@lanternhillpr.com</li>
      <li><svg viewBox="0 0 24 24"><path d="M12 2a10 10 0 1 0 0 20 10 10 0 0 0 0-20zm0 2c.9 0 2.2 1.9 2.7 5H9.3C9.8 5.9 11.1 4 12 4zM4.3 11h3a15 15 0 0 1 .1-2H5a8 8 0 0 0-.7 2zm0 2c.1.7.4 1.4.7 2h2.4a15 15 0 0 1-.1-2zm5 0h5.4a13 13 0 0 1-.2 2H9.5a13 13 0 0 1-.2-2zm0-2a13 13 0 0 1 .2-2h5a13 13 0 0 1 .2 2zm7.4 0a15 15 0 0 0-.1-2H19a8 8 0 0 1 .7 2zm0 2h3a8 8 0 0 1-.7 2h-2.4a15 15 0 0 0 .1-2zM12 20c-.9 0-2.2-1.9-2.7-3h5.4c-.5 1.1-1.8 3-2.7 3z"/></svg>www.lanternhillpr.com</li>
    </ul>
    <p class="address">88 Franklin Street, Brooklyn NY, 11222.</p>
  </section>

  <section class="card card--back">
    <h2 class="wordmark">
      <span class="wordmark__main">Lantern Hill</span>
      <span class="wordmark__sub">Publicity</span>
    </h2>
  </section>
</main>
</body>
</html>
```